Eye Catching Stylish Seminar Flyer

Design a Business Seminar Flyer that will be used for Print and Web distribution that is professional, eye catching in its color scheme and fonts.

have www.bluelanternforum.example to register

Target Market(s)

Who is this for: business owners, marketplace professionals, homemakers.

Industry/Entity Type

Business Consultant

Font styles to use
Serif

Colors
abd037

Requirements
Must have
• Great colors, great Font
Nice to have
• Design a simple professional text based Logo for the Event that encapsulates For the flyer. Eye catching designs that provoke action in the reader of the flyer.
Should not have
• Cross designs stereotypical designs that are associated with religion. Rather they should be creative toward people that own businesses and work with colleagues in a daily office, school etc.

```html
<!DOCTYPE html>
<html lang="en">
<head>
<meta charset="utf-8">
<title>The Voice of the Lord in the Marketplace – Seminar Flyer</title>
<link href="https://fonts.googleapis.com/css2?family=Cinzel:wght@400;600&family=Tinos:wght@400;700&display=swap" rel="stylesheet">
<style>
  :root {
    --maroon: #7e1c2e;
    --orange: #c9522b;
    --ink: #161616;
    --paper: #ffffff;
    --leaf-tint: #f2f2f2;
    --backdrop: #2e2e2e;
  }
  * { margin: 0; padding: 0; box-sizing: border-box; }
  html, body { width: 960px; height: 1200px; overflow: hidden; background: var(--backdrop); }
  .flyer {
    position: absolute; left: 71px; top: 20px;
    width: 818px; height: 1160px;
    background: var(--paper); overflow: hidden;
    font-family: "Tinos", "Times New Roman", serif;
  }
  .decor { position: absolute; inset: 0; }
  .title { position: absolute; left: 69px; top: 58px; width: 700px; height: 170px; font-family: "Cinzel", serif; color: var(--maroon); font-weight: 400; }
  .title span { position: absolute; white-space: nowrap; line-height: 1; }
  .title-the { left: 0; top: 0; font-size: 148px; letter-spacing: -4px; transform: scaleX(0.8); transform-origin: left top; }
  .title-voice { left: 248px; top: 20px; font-size: 62px; color: var(--orange); }
  .title-lord { left: 246px; top: 74px; font-size: 102px; font-weight: 600; }
  .subtitle { position: absolute; left: 69px; top: 234px; font-family: "Cinzel", serif; font-size: 58px; line-height: 66px; white-space: nowrap; }
  .subtitle .line { display: block; }
  .subtitle .ink { color: var(--ink); }
  .subtitle .accent { color: var(--orange); font-weight: 600; }
  .subtitle .strong { color: var(--maroon); font-weight: 600; }
  .tag { position: absolute; left: 69px; }
  .tag svg { position: absolute; inset: 0; }
  .tag span { position: relative; display: block; color: #fff; padding-left: 28px; white-space: nowrap; }
  .tag-dates { top: 465px; width: 230px; height: 52px; }
  .tag-dates span { font-size: 38px; line-height: 52px; }
  .tag-fee { top: 647px; width: 325px; height: 72px; }
  .tag-fee span { font-size: 52px; line-height: 70px; font-weight: 700; }
  .schedule { position: absolute; left: 69px; top: 546px; font-size: 26px; line-height: 44px; color: var(--ink); }
  .schedule b { color: var(--maroon); }
  .fee-note { position: absolute; left: 69px; top: 738px; font-size: 24px; line-height: 33px; color: var(--ink); }
  .featuring { position: absolute; left: 69px; top: 816px; }
  .featuring h2 { font-size: 24px; color: var(--orange); font-weight: 700; margin-bottom: 8px; }
  .featuring li { list-style: none; font-size: 19px; line-height: 32px; color: var(--ink); }
  .featuring li span { color: var(--maroon); }
  .band { position: absolute; left: 0; top: 1020px; }
  .band-text { position: absolute; left: 69px; top: 1057px; color: #fff; font-size: 23px; display: flex; align-items: center; gap: 10px; white-space: nowrap; }
  .brand { position: absolute; left: 462px; top: 984px; width: 266px; text-align: center; }
  .brand-mark { display: block; width: 46px; height: 46px; margin: 0 auto 14px; background: var(--maroon); }
  .brand-name { display: block; font-family: "Cinzel", serif; color: var(--maroon); font-size: 28px; line-height: 32px; font-weight: 400; white-space: nowrap; }
</style>
</head>
<body>
<main class="flyer">
  <svg class="decor" width="818" height="1160" role="img" aria-label="Faint leaf and branch decoration">
    <polygon points="540,0 818,0 818,1160 700,1160 455,750 620,420 560,260" fill="var(--leaf-tint)"/>
  </svg>

  <h1 class="title">
    <span class="title-the">The</span>
    <span class="title-voice">Voice of</span>
    <span class="title-lord">Lord</span>
  </h1>

  <p class="subtitle">
    <span class="line"><span class="ink">In the </span><span class="accent">Marketplace:</span></span>
    <span class="line ink">Moving from</span>
    <span class="line strong">Intimacy to Impact</span>
  </p>

  <div class="tag tag-dates">
    <svg width="230" height="52" aria-hidden="true">
      <polygon points="0,0 218,0 230,26 218,52 0,52" fill="var(--maroon)"/>
      <polygon points="0,0 208,0 220,26 208,52 0,52" fill="var(--orange)"/>
    </svg>
    <span>DATES</span>
  </div>

  <p class="schedule">
    <b>March 24th</b> 6pm-9:20pm<br>
    <b>March 25th</b> 8:30am-2:20pm
  </p>

  <div class="tag tag-fee">
    <svg width="325" height="72" aria-hidden="true">
      <polygon points="0,0 310,0 325,36 310,72 0,72" fill="var(--maroon)"/>
      <polygon points="0,0 298,0 313,36 298,72 0,72" fill="var(--orange)"/>
    </svg>
    <span>FEE: $30</span>
  </div>

  <p class="fee-note">Includes continental breakfast, lunch,<br>and light refreshments throughout the conference.</p>

  <section class="featuring">
    <h2>Featuring</h2>
    <ul>
      <li>Marcus Whitfield: <span>Author/Podcaster</span></li>
      <li>Daniel Reyes: <span>Business leader/Trainer</span></li>
      <li>Clara Whitfield: <span>Writer</span></li>
      <li>Sofia Marquez: <span>Business Owner</span></li>
      <li>Thomas Keller: <span>Business Owner</span></li>
    </ul>
  </section>

  <svg class="band" width="818" height="102" aria-hidden="true">
    <polygon points="0,0 455,0 430,51 455,102 0,102" fill="var(--maroon)"/>
    <polygon points="733,0 818,0 818,102 733,102 753,51" fill="var(--orange)"/>
  </svg>
  <p class="band-text">
    <svg width="20" height="20" viewBox="0 0 22 22" aria-hidden="true">
      <g fill="none" stroke="#fff" stroke-width="1.6">
        <circle cx="11" cy="11" r="9.5"/>
        <ellipse cx="11" cy="11" rx="4.2" ry="9.5"/>
        <line x1="1.5" y1="11" x2="20.5" y2="11"/>
        <line x1="3" y1="6" x2="19" y2="6"/>
        <line x1="3" y1="16" x2="19" y2="16"/>
      </g>
    </svg>
    www.bluelanternforum.example
  </p>

  <div class="brand">
    <span class="brand-mark"></span>
    <span class="brand-name">Blue Lantern</span>
    <span class="brand-name">Forum</span>
  </div>
</main>
</body>
</html>
```